Plakat-Design für Online-Vertrieb von Messeständen an Unternehmen
Zielgruppe
Wir verkaufen über unseren Onlineshop (www.standwerk-beispiel.de) Messestände an Unternehmen.
Aufgabenstellung
Wir benötigten eine Grafik, die auf unseren Messeständen als Beispiel eingebunden werden kann. Sie soll unseren Kunden die Möglichkeit geben, dass sie sich das System besser vorstellen können. Da wir das System RAVOK nennen werden, befindet sich das dazugehörige Logo in der Anlage. Das Logo sollte auf dem Design sichtbar sein, aber muss nicht im Vordergrund stehen.
Das Messesystem ist variabel und in vielen verschiedenen Breiten und Formationen aufstellbar. Die Grafik muss bei Eckständen auch mal um die Ecke laufen. Somit wäre es perfekt, wenn die Grafik für verschiedene Breiten erweiterbar wäre. Die Standardhöhe des Systems liegt immer bei 2,5m.
Zwei Beispielvarianten mit blanko Grafik liegen in der Anlage und können gerne für die Visualisierung verwendet werden.
Gerne kann auch ein einfacher Farbverlauf mit modernen Farben verwendet werden. Wir sind hier aber sehr flexibel.
Die Messestände haben eine LED-Hinterleuchtung in ihren Motiven, sodass sie in Realität strahlend wirken.
Wenn wir ein Motiv finden würden, mit dem wir den 'Strahleffekt' gut visualisieren könnten, wäre das natürlich hervorragend.
Im folgenden finden Sie andere Beispiele von Messeständen inkl. Stoffgrafiken. Hier sieht man auch die variablen Standgrößen, welche eine Erweiterbarkeit des Motivs erforderlich machen.
Fast identisch zu unserem neuen System sind die Artikel in der Kategorie 'LED Messestand Stoff' (https://www.standwerk-beispiel.de/Messestand/LED-Messestand-Stoff/)
Ansonsten sind hier aber noch weitere Beispiele:
https://www.standwerk-beispiel.de/Messestand/Messestand-Stoff/
https://www.standwerk-beispiel.de/Messestand/LED-Messestand-Stoff/
https://www.standwerk-beispiel.de/Messebausysteme/TORVANE-MO/
https://www.standwerk-beispiel.de/Messebausysteme/Quorin/Quorin-BildFront/
https://www.standwerk-beispiel.de/Messebausysteme/Quorin/Quorin-WeitTuch/

```html
<!DOCTYPE html>
<html lang="de">
<head>
<meta charset="utf-8">
<title>RAVOK – LED-Messewand Motiv</title>
<link href="https://fonts.googleapis.com/css2?family=Barlow+Condensed:wght@500;700&display=swap" rel="stylesheet">
<style>
  :root {
    --stage: #e9e6e1;
    --night: #050302;
    --deep-bronze: #2a1606;
    --bronze: #7a4a12;
    --gold: #d99a2b;
    --glow: #ffd77a;
    --brand-yellow: #f5b800;
    --white: #ffffff;
  }
  html, body {
    margin: 0;
    padding: 0;
    width: 1200px;
    height: 900px;
    overflow: hidden;
    background: var(--stage);
  }
  .canvas {
    position: relative;
    width: 1200px;
    height: 900px;
  }
  .wall-graphic {
    position: absolute;
    left: 60px;
    top: 205px;
    width: 1080px;
    height: 490px;
    overflow: hidden;
    background: var(--night);
    box-shadow: 0 10px 30px rgba(0,0,0,0.18);
  }
  .motif {
    position: absolute;
    inset: 0;
    background:
      radial-gradient(circle at 44% 40%, var(--glow) 0, rgba(255,215,122,0.6) 2%, rgba(217,154,43,0.25) 7%, transparent 13%),
      radial-gradient(ellipse 32% 60% at 78% 55%, var(--gold) 0, var(--bronze) 45%, transparent 80%),
      radial-gradient(ellipse 40% 30% at 25% 85%, rgba(217,154,43,0.55) 0, rgba(122,74,18,0.35) 50%, transparent 80%),
      radial-gradient(ellipse 30% 25% at 95% 90%, rgba(255,215,122,0.5) 0, transparent 70%),
      linear-gradient(160deg, var(--night) 0%, var(--night) 35%, var(--deep-bronze) 70%, var(--bronze) 100%);
  }
  .brand {
    position: absolute;
    left: 257px;
    top: 38px;
    font-family: "Barlow Condensed", sans-serif;
  }
  .brand-name {
    display: flex;
    align-items: center;
    gap: 8px;
    margin: 0;
    font-weight: 700;
    font-size: 56px;
    line-height: 1;
    letter-spacing: 1px;
    color: var(--brand-yellow);
  }
  .brand-mark {
    width: 12px;
    height: 12px;
    background: var(--brand-yellow);
  }
  .brand-byline {
    margin: 6px 0 0;
    font-weight: 500;
    font-size: 15px;
    letter-spacing: 0.5px;
    color: var(--white);
  }
</style>
</head>
<body>
  <main class="canvas">
    <section class="wall-graphic">
      <div class="motif" role="img" aria-label="Hinterleuchtetes Motiv: Frau mit goldener Körperfarbe im Profil, hält auf der offenen Hand einen strahlenden Lichtfunken, umgeben von goldenen Bokeh-Lichtern auf schwarzem Grund"></div>
      <div class="brand">
        <p class="brand-name">RAVOK<span class="brand-mark"></span></p>
        <p class="brand-byline">by STANDWERK-BEISPIEL.DE</p>
      </div>
    </section>
  </main>
</body>
</html>
```